Book Cover Project

This is a printed journal front and back cover design. We like the current design, but it feels a little too flat / too simple.

NOTE: we are not looking for a total makeover, just a finishing / polishing of this cover.

Here is our other book cover: https://www.shelvorix.com/Mat-Studio-Blueprint-Calm-Days/dp/7390462815/ref=tmm_hrd_swatch_0?_encoding=UTF8&qid=&sr=
it's purple and yellow (mostly purple)
this one is yellow and we're thinking to add a purple bar at the bottom

Specs: 6 in x 9 in full bleed for print

```html
<!DOCTYPE html>
<html lang="en">
<head>
<meta charset="utf-8">
<title>Steady Stride Notebook – Cover</title>
<link rel="stylesheet" href="https://fonts.googleapis.com/css2?family=Open+Sans:wght@400;600&display=swap">
<style>
  :root {
    --page-bg: #e6e6e6;
    --cover-yellow: #ebc603;
    --ink: #0b0b0b;
    --accent-purple: #4a4896;
    --art-dark: #1a1a1a;
    --art-mid: #3a3208;
  }
  * { margin: 0; padding: 0; box-sizing: border-box; }
  html, body {
    width: 1200px;
    height: 800px;
    overflow: hidden;
    background: var(--page-bg);
  }
  .canvas {
    position: relative;
    width: 1200px;
    height: 800px;
  }
  .cover {
    position: absolute;
    left: 408px;
    top: 93px;
    width: 397px;
    height: 607px;
    background: var(--cover-yellow);
    color: var(--ink);
    overflow: hidden;
    font-family: "Open Sans", "Helvetica Neue", Arial, sans-serif;
  }
  .cover-title { font-weight: 600; }
  .cover-line {
    position: absolute;
    left: 0;
    width: 100%;
    text-align: center;
    line-height: 1;
    white-space: nowrap;
  }
  .title-first  { top: 40px;  font-size: 72px; font-weight: 600; }
  .title-second { top: 138px; font-size: 50px; font-weight: 600; }
  .title-third  { top: 191px; font-size: 44px; font-weight: 600; }
  .runner-art {
    position: absolute;
    left: 144px;
    top: 250px;
    width: 111px;
    height: 255px;
    border-radius: 50px;
    background: radial-gradient(ellipse at 50% 45%, var(--art-dark) 0%, var(--art-mid) 55%, var(--cover-yellow) 100%);
  }
  .tagline {
    top: 524px;
    font-size: 17px;
    font-weight: 600;
    letter-spacing: 1.6px;
  }
  .author {
    top: 552px;
    font-size: 27px;
    font-weight: 400;
  }
  .accent-bar {
    position: absolute;
    left: 0;
    bottom: 0;
    width: 100%;
    height: 18px;
    background: var(--accent-purple);
  }
</style>
</head>
<body>
  <main class="canvas">
    <section class="cover">
      <h1 class="cover-title">
        <span class="cover-line title-first">STEADY</span>
        <span class="cover-line title-second">STRIDE</span>
        <span class="cover-line title-third">NOTEBOOK</span>
      </h1>
      <div class="runner-art" role="img" aria-label="Black ink silhouette of a runner mid-stride, with paint splatter"></div>
      <p class="cover-line tagline">MOVE | REFLECT | GROW</p>
      <p class="cover-line author">ELIAS THORNBURY</p>
      <div class="accent-bar"></div>
    </section>
  </main>
</body>
</html>
```